Web Design Project - Homepage mockup for media services company

Client would like a site much like this example below in terms of design and layout:

http://plumtide.net/

It's a media services company and the services they provide are:
-audio/video production
-graphic design
-social media
-web development
-apparel design

Their logo file is attached. I have also attached some of their service descriptions if that at all helps with things.

```html
<!DOCTYPE html>
<html lang="en">
<head>
<meta charset="utf-8">
<title>R. Vantelli – Media Services</title>
<link href="https://fonts.googleapis.com/css2?family=Noto+Serif:wght@400;700&family=Sorts+Mill+Goudy&display=swap" rel="stylesheet">
<style>
:root{
  --wine:#6e1d1f;
  --wine-dark:#4e1214;
  --panel:#681f21;
  --ink:#1e1e1e;
  --paper:#ffffff;
  --footer:#3a3a3a;
  --footer-base:#222222;
  --link-blue:#3aa0e0;
}
*{margin:0;padding:0;box-sizing:border-box}
html,body{width:960px;height:1200px;overflow:hidden}
body{
  position:relative;
  font-family:"Noto Serif",Georgia,serif;
  color:var(--ink);
  background:
    radial-gradient(ellipse 520px 160px at 480px 60px,#f2f2f2 0%,rgba(242,242,242,0) 100%),
    radial-gradient(ellipse 600px 320px at 480px 560px,#d0d0d0 0%,rgba(208,208,208,0) 100%),
    linear-gradient(#e2e2e2 0%,#b0b0b0 24%,#c4c4c4 45%,#bdbdbd 70%,#a8a8a8 100%);
}
.abs{position:absolute}
.display{font-family:"Sorts Mill Goudy",Georgia,serif;font-weight:400}

/* header */
.brand{left:92px;top:14px;display:flex;align-items:center;gap:10px}
.brand-dot{width:88px;height:88px;border-radius:50%;background:#2a2a2a;border:4px solid #555}
.brand-name{font-family:"Noto Serif",Georgia,serif;font-size:34px;color:#2a2a2a}
.call{left:628px;top:32px;font-size:14px;color:#333}
.call b{font-size:18px;color:var(--wine);font-weight:400}
.social{display:flex;gap:7px}
.social span{width:24px;height:24px;border-radius:50%;background:#555;display:block}
.social-top{left:814px;top:33px}
.nav{left:472px;top:82px;display:flex;gap:14px;font-size:15px;color:#2a2a2a;white-space:nowrap}
.nav .current{color:#8b1e22}

/* slider */
.slider{left:95px;top:120px;width:774px;height:335px;display:flex;box-shadow:0 2px 6px rgba(0,0,0,.35)}
.slide-photo{width:459px;height:100%;background:radial-gradient(circle at 40% 50%,#5b4f4c 0%,#2a2a2a 45%,#141414 100%)}
.slide-panel{flex:1;background:var(--panel);color:#f3e6e6;padding:42px 20px 0 27px}
.slide-panel h2{font-size:33px;line-height:29px;color:#fff;margin-bottom:13px}
.slide-panel li{list-style:none;font-size:13.5px;height:28.8px;display:flex;align-items:center;gap:9px}
.slide-panel li svg{flex:none}
.arrow{width:32px;height:32px;border-radius:50%;background:#0d0d0d;top:262px;display:flex;align-items:center;justify-content:center}
.arrow-prev{left:80px}
.arrow-next{left:848px}

/* intro */
.welcome{left:95px;top:472px;width:455px}
.welcome h1{font-size:33px;color:var(--wine);margin-bottom:8px;line-height:40px}
.welcome p{font-size:10.6px;line-height:15.2px;text-align:justify}
.testimonials{left:588px;top:470px;width:282px}
.testimonials h2{font-size:23px;color:var(--wine);display:flex;align-items:center;gap:8px;line-height:34px}
.testimonials .quote-mark{font-size:60px;color:#888;line-height:30px;height:30px;margin-top:12px}
.testimonials p{font-size:10.6px;line-height:15.2px;text-align:justify;margin:6px 0 0 3px}
.testimonials cite{display:block;font-style:normal;color:var(--wine);font-size:10.6px;margin-left:3px}

/* services */
.services-sheet{left:78px;top:626px}
.services-title{left:80px;top:664px;width:794px;text-align:center;font-size:19px;font-weight:400;color:#111}
.service{top:714px;width:150px;text-align:center;font-size:14.5px;line-height:15.5px;color:var(--wine-dark)}
.service-icon{width:92px;height:92px;border-radius:50%;margin:0 auto 24px;
  display:flex;align-items:center;justify-content:center;
  background:radial-gradient(circle at 50% 35%,#ffffff 0%,#e6e6e6 60%,#c9c9c9 100%);
  box-shadow:0 0 0 1px #c6c6c6,0 8px 6px -4px rgba(0,0,0,.15)}
.service-icon i{display:block;width:60px;height:60px;border-radius:50%;background:radial-gradient(circle,var(--tone) 0%,rgba(255,255,255,0) 70%);opacity:.75}

/* footer */
.footer{left:0;top:934px;width:960px;height:200px;background:var(--footer)}
.quote-title{left:88px;top:954px;font-size:23px;color:#f0f0f0}
.field{background:linear-gradient(#8d8d8d,#b4b4b4);border:1px solid #9a9a9a;border-radius:2px;font-size:11px;color:#3a3a3a;padding:9px 7px}
.field-name{left:90px;top:992px;width:228px;height:32px}
.field-email{left:90px;top:1033px;width:228px;height:32px}
.field-service{left:327px;top:992px;width:229px;height:73px}
.submit{left:90px;top:1076px;width:126px;height:37px;background:linear-gradient(#8c1b1f,#4f0d10);color:#fff;font-size:14px;display:flex;align-items:center;justify-content:center;border-radius:2px;box-shadow:0 1px 2px rgba(0,0,0,.5)}
.tweets-title{left:608px;top:954px;font-size:23px;color:#f0f0f0;display:flex;align-items:center;gap:10px}
.tweets-title span{width:17px;height:17px;background:var(--link-blue);border-radius:3px;display:block}
.tweet{left:610px;width:260px;font-size:10.6px;line-height:14.4px;color:#eee}
.tweet a{color:var(--link-blue);text-decoration:none}
.base{left:0;top:1134px;width:960px;height:66px;background:var(--footer-base)}
.base-links{left:88px;top:1149px;display:flex;gap:12px;font-size:12.5px;color:#bdbdbd}
.base-links span:first-child{color:#e6e6e6}
.copyright{left:88px;top:1169px;font-size:10.5px;color:#555}
.social-base{left:801px;top:1154px}
.social-base span{background:#8a8a8a}
</style>
</head>
<body>

<header>
  <div class="abs brand"><span class="brand-dot"></span><span class="brand-name">R. Vantelli</span></div>
  <div class="abs call">Call us at <b>012 555 0147</b></div>
  <div class="abs social social-top"><span aria-label="Social profile one"></span><span aria-label="Social profile two"></span></div>
  <nav class="abs nav">
    <span class="current">HOME</span><span>ABOUT US</span>
    <span>SERVICES <svg width="11" height="9" viewBox="0 0 11 9"><path d="M1 2l4.5 4.5L10 2" fill="none" stroke="#2a2a2a" stroke-width="2.4"/></svg></span>
    <span>WORKS</span><span>CONTACT US</span>
  </nav>
</header>

<section class="abs slider">
  <div class="slide-photo" role="img" aria-label="Photo of a woman listening on studio headphones against a dark speaker grille"></div>
  <div class="slide-panel">
    <h2 class="display">Audio Production Services</h2>
    <ul>
      <li><svg width="8" height="11" viewBox="0 0 8 11"><path d="M1.5 1l4.5 4.5L1.5 10" fill="none" stroke="#e8d6d6" stroke-width="2"/></svg>Voice Over Recording</li>
      <li><svg width="8" height="11" viewBox="0 0 8 11"><path d="M1.5 1l4.5 4.5L1.5 10" fill="none" stroke="#e8d6d6" stroke-width="2"/></svg>Sound Effects Recording</li>
      <li><svg width="8" height="11" viewBox="0 0 8 11"><path d="M1.5 1l4.5 4.5L1.5 10" fill="none" stroke="#e8d6d6" stroke-width="2"/></svg>Production Sound Mixing</li>
      <li><svg width="8" height="11" viewBox="0 0 8 11"><path d="M1.5 1l4.5 4.5L1.5 10" fill="none" stroke="#e8d6d6" stroke-width="2"/></svg>Foley</li>
      <li><svg width="8" height="11" viewBox="0 0 8 11"><path d="M1.5 1l4.5 4.5L1.5 10" fill="none" stroke="#e8d6d6" stroke-width="2"/></svg>Fully Produced Score</li>
      <li><svg width="8" height="11" viewBox="0 0 8 11"><path d="M1.5 1l4.5 4.5L1.5 10" fill="none" stroke="#e8d6d6" stroke-width="2"/></svg>Orchestration and Arranging</li>
      <li><svg width="8" height="11" viewBox="0 0 8 11"><path d="M1.5 1l4.5 4.5L1.5 10" fill="none" stroke="#e8d6d6" stroke-width="2"/></svg>Music For Live Media</li>
    </ul>
  </div>
</section>
<div class="abs arrow arrow-prev"><svg width="10" height="12" viewBox="0 0 10 12"><path d="M7 1.5L2.5 6 7 10.5" fill="none" stroke="#fff" stroke-width="2.6"/></svg></div>
<div class="abs arrow arrow-next"><svg width="10" height="12" viewBox="0 0 10 12"><path d="M3 1.5L7.5 6 3 10.5" fill="none" stroke="#fff" stroke-width="2.6"/></svg></div>

<section class="abs welcome">
  <h1 class="display">Welcome to R. Vantelli</h1>
  <p>Lorem ipsum dolor sit amet, consectetur adipiscing elit. Sed est turpis, facilisis in pretium lobortis, imperdiet et lectus. Donec et elit mauris. Etiam diam risus, dapibus sed interdum ut, fringilla et turpis. Pellentesque lobortis velit ac quam ornare ultricies. Etiam aliquam vehicula metus, sit amet blandit nunc ornare eget. Etiam a adipiscing augue. Pellentesque consequat sem id lacus fringilla vulputate. Mauris egestas elementum leo, et tincidunt arcu sodales a.</p>
</section>

<aside class="abs testimonials">
  <h2 class="display">Client Testimonials <span class="quote-mark">“</span></h2>
  <p>Duis congue sollicitudin sem, sed mollis purus cursus sit amet. Sed faucibus velit at libero cursus interdum. Vivamus et libero quis leo accumsan rutrum. Curabitur dolor sem,</p>
  <cite>-Daniel Ortis</cite>
</aside>

<svg class="abs services-sheet" width="800" height="280" viewBox="0 0 800 280">
  <defs>
    <filter id="sheet-shadow" x="-5%" y="-10%" width="110%" height="130%">
      <feDropShadow dx="0" dy="8" stdDeviation="5" flood-color="#000" flood-opacity=".35"/>
    </filter>
  </defs>
  <path d="M30 24 L782 18 Q788 140 796 268 Q500 272 240 262 Q90 256 2 242 Q28 210 30 160 Z" fill="var(--paper)" filter="url(#sheet-shadow)"/>
  <rect x="348" y="2" width="120" height="20" fill="#e9e9e9" opacity=".85"/>
</svg>
<h2 class="abs services-title">SERVICES WE OFFER</h2>

<div class="abs service" style="left:108px"><div class="service-icon" role="img" aria-label="Film reel icon"><i style="--tone:#8a8a8a"></i></div>AUDIO/VIDEO<br>PRODUCTION</div>
<div class="abs service" style="left:257px"><div class="service-icon" role="img" aria-label="Paint palette icon"><i style="--tone:#c9a46a"></i></div>GRAPHIC<br>DESIGN</div>
<div class="abs service" style="left:406px"><div class="service-icon" role="img" aria-label="Blue bird on a perch icon"><i style="--tone:#3d8fd8"></i></div>SOCIAL<br>MEDIA</div>
<div class="abs service" style="left:555px"><div class="service-icon" role="img" aria-label="Globe with magnifier icon"><i style="--tone:#2f6fb8"></i></div>WEB<br>DEVELOPMENT</div>
<div class="abs service" style="left:703px"><div class="service-icon" role="img" aria-label="Yellow shirt icon"><i style="--tone:#f2d32c"></i></div>APPAREL<br>DESIGN</div>

<footer>
  <div class="abs footer"></div>
  <h2 class="abs quote-title display">Request a Quote</h2>
  <div class="abs field field-name">Your Name</div>
  <div class="abs field field-email">Your Email ID</div>
  <div class="abs field field-service">Service Required</div>
  <div class="abs submit">SUBMIT</div>

  <h2 class="abs tweets-title display">Recent Tweets <span></span></h2>
  <p class="abs tweet" style="top:990px">Morbi non nunc mauris, pretium malesuada lectus. Ut id ligula id felis accumsan <a>http://lnk.to/QWMRPL</a><br><a>2 days ago</a>.</p>
  <p class="abs tweet" style="top:1047px">Curabitur sed lacus at mi gravida ultrices. In hac habitasse platea dictumst.<br><a>http://lnk.to/QWPLMRTS 4 days ago</a>.</p>

  <div class="abs base"></div>
  <nav class="abs base-links">
    <span>Home</span><span>About us</span><span>Services</span><span>Works</span><span>Contact us</span><span>Testimonials</span><span>Terms &amp; Conditions</span><span>Privacy Policy</span>
  </nav>
  <div class="abs copyright">Copyright © R. Vantelli. All rights reserved.</div>
  <div class="abs social social-base"><span aria-label="Social profile one"></span><span aria-label="Social profile two"></span></div>
</footer>

</body>
</html>
```